BUSINESS book cover

Publishing a book for a specific industry and hope to customize it for different industries in the future. So, design needs to be flexible. I want BRIGHT (possibly orange) cover with large words for title...really do not need illustration. Just the subtitle will change for future editions. Book is going to be 5.25" x 8"

Sorry for any confusion. The title of the book is: "Once You Reach a Yes..." The subtitle is: A Comprehensive Member Expderience Guide for Today's Club Management Professional

```html
<!DOCTYPE html>
<html lang="en">
<head>
<meta charset="utf-8">
<title>Once You Reach a Yes... — Book Cover</title>
<link rel="stylesheet" href="https://fonts.googleapis.com/css2?family=Anton&family=Oswald:wght@500;600;700&family=PT+Sans+Narrow:wght@400;700&display=swap">
<style>
  :root {
    --cover-orange: #ff3300;
    --title-white: #ffffff;
    --body-navy: #1d2550;
    --subtitle-yellow: #f7c400;
    --author-ink: #16181f;
    --photo-tone: #8c8c8c;
  }
  * { margin: 0; padding: 0; box-sizing: border-box; }
  html, body { width: 1200px; height: 870px; overflow: hidden; background: var(--cover-orange); }
  .cover {
    position: relative; width: 1200px; height: 870px; overflow: hidden;
    background: var(--cover-orange);
  }
  .wrap-edge, .spine, .front-art { position: absolute; top: 0; }
  .wrap-edge { left: 0; width: 40px; height: 870px; }
  .spine { left: 575px; width: 50px; height: 870px; }
  .front-art { left: 630px; width: 570px; height: 870px; }
  .title-text { font-family: "Anton", sans-serif; fill: var(--title-white); }
  .subtitle-text { font-family: "Oswald", sans-serif; font-weight: 600; fill: var(--subtitle-yellow); }
  .author-text { font-family: "Oswald", sans-serif; font-weight: 700; fill: var(--author-ink); }

  .back {
    position: absolute; left: 62px; top: 36px; width: 485px;
    font-family: "PT Sans Narrow", sans-serif; font-weight: 700;
    color: var(--body-navy); font-size: 17px; line-height: 19px;
  }
  .back-headline { color: var(--title-white); font-size: 24px; line-height: 28px; margin-bottom: 6px; }
  .back p { text-align: justify; margin-bottom: 9px; }
  .back .lead-in { color: var(--title-white); }
  .benefits { list-style: none; margin: 9px 0 9px 34px; }
  .benefits li { padding-left: 6px; text-indent: -6px; }
  .benefits li::before { content: "· "; }
  .closing { margin-left: 34px; }

  .author-photo {
    position: absolute; left: 63px; top: 587px; width: 192px; height: 137px;
    background: linear-gradient(135deg, #b5b5b5, var(--photo-tone) 55%, #3d3d3d);
  }
  .author-bio {
    position: absolute; left: 265px; top: 588px; width: 283px;
    font-family: "PT Sans Narrow", sans-serif; font-size: 13px; line-height: 15px;
    color: var(--body-navy); text-align: justify;
  }
</style>
</head>
<body>
<main class="cover">

  <svg class="wrap-edge" width="40" height="870" viewBox="0 0 40 870" aria-hidden="true">
    <text class="title-text" font-size="56" transform="translate(-6 18) rotate(90)" textLength="880" lengthAdjust="spacingAndGlyphs">ONCE YOU REACH A YES...</text>
  </svg>

  <section class="back">
    <h2 class="back-headline">This book is for club management professionals only!</h2>
    <p>Why is Brewhouse so successful in selling you a $4.00 cup of coffee when QuickBite charges $2.00?</p>
    <p>Why does a stay at a Grand Meridian hotel seem much different than at a stay at the Roadside Lodge?</p>
    <p>Most people today would answer that it’s all about ‘customer service’ when, in fact, they would be wrong! Both QuickBite and Roadside Lodge offer incredible customer service. What Brewhouse and Grand Meridian understand is that it is about the customer EXPERIENCE!</p>
    <p>Much attention is given to the member experience in this profession, but do you really understand what needs to be done to take your club to the next level?</p>
    <p><span class="lead-in">Once You Reach a Yes...</span> is a comprehensive book with assessments, surveys and examples personalized to the club management profession.</p>
    <p>In reading this book, you will be able to:</p>
    <ul class="benefits">
      <li>Analyze and tweak our member touch points</li>
      <li>Create a “touch point map” specific to your club</li>
      <li>Assess whether or not your strategy will be successful</li>
      <li>Be more innovative in managing your people and your members</li>
      <li>Take an innovation survey</li>
      <li>Establish your club’s “Declaration of Experience”</li>
      <li>Distinguish between employee engagement and employee satisfaction</li>
    </ul>
    <p class="closing">And much, much more.</p>
  </section>

  <div class="author-photo" role="img" aria-label="Black and white portrait photo of the author"></div>
  <p class="author-bio">Dana Marlow M.Ed, CSP has been working with club professionals for 15+ years. Her first book, “Thinking Past the Edges” has long been an industry favorite and her sessions at NCMA nationally and for individual clubs have made her a leading expert in creative thinking as it applies to the member experience. For more information on booking Dana, visit www.DanaMarlow.com or call her directly at 555-014-2290</p>

  <svg class="spine" width="50" height="870" viewBox="0 0 50 870" aria-label="Spine">
    <text class="title-text" font-size="44" transform="translate(8 32) rotate(90)" textLength="560" lengthAdjust="spacingAndGlyphs">ONCE YOU REACH A YES...</text>
    <text class="author-text" font-size="26" transform="translate(14 640) rotate(90)" textLength="178" lengthAdjust="spacingAndGlyphs">DANA MARLOW, <tspan font-size="18">M.ED, CSP</tspan></text>
  </svg>

  <svg class="front-art" width="570" height="870" viewBox="630 0 570 870" aria-label="Front cover">
    <defs>
      <filter id="title-shadow" x="-5%" y="-5%" width="110%" height="115%">
        <feDropShadow dx="2" dy="3" stdDeviation="2" flood-color="#7a1400" flood-opacity="0.55"/>
      </filter>
    </defs>
    <g filter="url(#title-shadow)">
      <text class="title-text" x="644" y="130" font-size="98" textLength="537" lengthAdjust="spacingAndGlyphs">ONCE YOU</text>
      <text class="title-text" x="648" y="342" font-size="198" textLength="525" lengthAdjust="spacingAndGlyphs">REACH</text>
      <text class="title-text" x="915" y="409" font-size="48" text-anchor="middle">A</text>
      <text class="title-text" x="641" y="609" font-size="186" textLength="538" lengthAdjust="spacingAndGlyphs">YES...</text>
    </g>
    <text class="subtitle-text" x="644" y="674" font-size="37" textLength="537" lengthAdjust="spacingAndGlyphs">A COMPREHENSIVE MEMBER EXPERIENCE GUIDE</text>
    <text class="subtitle-text" x="644" y="713" font-size="37" textLength="543" lengthAdjust="spacingAndGlyphs">FOR TODAY'S CLUB MANAGEMENT PROFESSIONAL</text>
    <text class="author-text" x="692" y="835" font-size="64" textLength="439" lengthAdjust="spacingAndGlyphs">DANA MARLOW, <tspan font-size="44">M.ED, CSP</tspan></text>
  </svg>

</main>
</body>
</html>
```